Mr K's - CD Cover Project number 6

Hi All,

I manage a small sound recording studio and need assistance with CD artwork, notably converting pdf image files to Photoshop, on print-ready templates, to submit to my CD duplication and packaging service

CD Name: “Walk On Lightly”, artist's name: “Mr. K’s Fine Tonic”.

In addition to the technical skill required to convert my images to Photoshop format, some creative design flair is desirable: the attractive superimposition of text (e.g., CD title and artist, liner notes, song titles, etc.) onto images, and the creation of professional-looking CD labels, is also required.

So I need a cover created using the images provided with the title and details superimposed.

I have planned on a folded rectangular insert to give 4 squarish pages – printed in color on one side of the rectangle, and monochromatic on the other.

I have executed this as a mock up, which you can view in 2 scans [ "...007jpg" and "...005.jpg" ]. Again, these scans are only of the mockup. (Source photos from which the mockups have been made are attached to this brie; others are available.)

The monochromatic side, once folded, would constitute the interior, i.e., where the text of the liner notes would be. It would be nice to see the text superimposed on a suitable background picture rendered lightly enough so as not to make the text difficult to read.

The color side would constitute the front "cover", or page 1 (visible through the plastic jewel case), and the back of the insert, or page 4. (The RIGHT-HAND SIDE of scan [“…007.jpeg”] would constitute the cover. The LEFT-HAND SIDE of the same scan would become the back of the insert.)

The name of the band [Mr. K’s Fine Tonic] , and the name of the CD [Walk On Lightly], would need to be added to page 1 (front cover, or RIGHT-HAND SIDE of scan [“…007.jpeg”] ) in some funky old (1920’s or 1930’s-style) font – without obscuring crucial parts of the various portraits.

(If a group portrait seems more suitable for the front cover than a collage of individual faces, a very good example is [ "Scan 110020032.jpeg" ] which could be substituted to advantage. This one already includes a likeness of the band's name.)

Pages 2 & 3 would consist of the text [see scan of mock up “.0005.jpg” ], i.e., the actual liner notes, provided in ".doc." file "WALK ON LIGHTLY liner notes & song list.docx".

The song list, also contained in the ".doc" file, needs to be added to the back tray card, which is mocked up as scan “.00046.jpeg”.

The "Tall Pine Records" logo [see ".psd" file] also needs to go on the back tray card.

The name of the band and the name of the CD need also to go on the spine (edge).

An attractive, monochromatic CD label needs to be designed. I would like it to feature the name of the band and the song list, superimposed on a lightly-rendered background photo.

If more pix are requested/desirable, I would be happy to provide additional ones.

Guidelines for setup are provided by the duplication company, "Sorvel". These are available at http://sorvel.platepressworks.example/Quoter/Templates.aspx

Target Market(s)

All ages, all socioeconomic groups, who like to have a good time.

Industry/Entity Type

Recording Studio

Requirements
Must have
• A funky, old-fashioned feel. The music is all from the 1920's and 1930's - honky tonk, blues, and "jug band" style. Therefore fonts, and artistic treatments should be reflective of those times, not modern, new age, psychedelic, or anything suggestive of "rock & roll".
Nice to have
• A lightly-rendered picture as a background picture for superimposed liner notes.
Should not have
• Anything flashy, modern, hyper-abstract, or rock & roll-ish.

```html
<!DOCTYPE html>
<html lang="en">
<head>
<meta charset="utf-8">
<title>Walk On Lightly – Liner Notes Spread</title>
<link href="https://fonts.googleapis.com/css2?family=Arimo:ital,wght@0,400;0,700;1,400&display=swap" rel="stylesheet">
<style>
  :root {
    --paper: #ffffff;
    --peach: #f1ab78;
    --peach-light: #f4b98b;
    --halftone: #8d8a86;
    --ink: #141414;
    --mark: #7a7a7a;
  }
  * { box-sizing: border-box; margin: 0; padding: 0; }
  html, body { width: 1200px; height: 766px; overflow: hidden; background: var(--paper); }
  .spread { position: relative; width: 1200px; height: 766px; }
  .trim-marks { position: absolute; inset: 0; }
  .page {
    position: absolute; top: 130px; height: 543px; width: 553px; overflow: hidden;
    font-family: "Arimo", Arial, sans-serif; font-weight: 700; color: var(--ink);
    font-size: 12px; line-height: 16.2px;
  }
  .page--left { left: 46px; }
  .page--right { left: 599px; }
  .page__photo { position: absolute; inset: 0; }
  .page__text { position: relative; padding: 5px 6px 0 6px; }
  .page--right .page__text { padding-left: 9px; padding-right: 4px; }
  .page__text p { margin-bottom: 12px; }
  .title { font-weight: 400; font-style: italic; }
</style>
</head>
<body>
<div class="spread">
  <svg class="trim-marks" width="1200" height="766" viewBox="0 0 1200 766">
    <g stroke="var(--mark)" stroke-width="1" fill="none">
      <line x1="0" y1="130" x2="32" y2="130"/><line x1="1168" y1="130" x2="1200" y2="130"/>
      <line x1="0" y1="672" x2="32" y2="672"/><line x1="1168" y1="672" x2="1200" y2="672"/>
      <line x1="46" y1="0" x2="46" y2="112"/><line x1="1152" y1="0" x2="1152" y2="112"/>
      <line x1="46" y1="690" x2="46" y2="766"/><line x1="1152" y1="690" x2="1152" y2="766"/>
      <line x1="598" y1="0" x2="598" y2="766" stroke-dasharray="2 3"/>
    </g>
  </svg>

  <section class="page page--left">
    <svg class="page__photo" role="img" aria-label="Lightly rendered halftone photo of the band playing guitars and jug instruments" width="553" height="543" viewBox="0 0 553 543" preserveAspectRatio="none">
      <defs>
        <radialGradient id="leftTone" cx="0.45" cy="0.55" r="0.7">
          <stop offset="0" stop-color="var(--halftone)" stop-opacity="0.55"/>
          <stop offset="1" stop-color="var(--halftone)" stop-opacity="0.15"/>
        </radialGradient>
      </defs>
      <rect width="553" height="543" fill="var(--peach)"/>
      <rect width="553" height="543" fill="url(#leftTone)"/>
    </svg>
    <div class="page__text">
      <p><span class="title">Mr. K’s Fine Tonic String &amp; Washboard Band</span> is a literal family of musicians who grew up together listening, singing and playing folk music, blues, spirituals, rounds, and whatever else seemed to improve a Maine campfire in August. Uncle Frank Hallorin, with his battered old Marlow guitar, was everybody’s inspiration.</p>
      <p>The rest of the year, childhood friend Ned Caskey kept the fires burning with his insatiable appetite for roots music, his driver’s license, and his enthusiasm for ferrying brothers Dale and Arlo to every coffee house and musical instrument store in Cambridge and Boston. Dale and Arlo in turn ferried their passion for blues and rags back to the Maine campfire. Arlo and Dale’s cousins, brothers Mack and Sid, caught the same bug. Other siblings and cousins did likewise. Friends Nora, Stan, and Boyd later joined in the musical mayhem.</p>
      <p>Lugging guitars, banjos and harmonicas, and playing folk music and blues, soon became a tradition of every sprawling family party, reunion, and holiday, year round. Friends asked Mr. K’s to play at their get-togethers, too. Anyone with an instrument was invited to join in. Then it was on to church suppers, talent shows, charity events, bicentennial celebrations, Old Home Days on New England village greens, and coffee houses.</p>
      <p><span class="title">Walk On Lightly</span>, the band’s first cassette, gained Mr. K’s entry into Hallard Square’s famous Nameless Tea Room’s huge 25th Anniversary New Talent Battle of the Bands. Mr. K’s earned a first-place finish, and coverage on the 11 o’clock news and Public Radio…and more notoriety and gigs. The genie was out of the bottle…for good</p>
      <p>1. <span class="title">Sunday Evening Stomp</span> &nbsp; Ishum Brady’s <span class="title">Sunday Stomp</span>, via Lenny Jarvis, featuring Boyd on the hurricane lamp chimney, and Mack’s insinuating bass.</p>
      <p>2. <span class="title">Taffy Peddler</span> &nbsp; The medicine show standard done live here with the band’s usual reckless abandon. Mack’s and Boyd’s frenetic response vocals steal the show.</p>
      <p>3. <span class="title">Walk On Lightly</span> &nbsp; Charlie Jessup’s contagious number about personal hygiene, with the refrain everybody <span class="title">sort of</span> gets…but not really. Mack provides his usual great backup vocals.</p>
    </div>
  </section>

  <section class="page page--right">
    <svg class="page__photo" role="img" aria-label="Lightly rendered halftone photo of band members with washboard and guitars" width="553" height="543" viewBox="0 0 553 543" preserveAspectRatio="none">
      <defs>
        <radialGradient id="rightTone" cx="0.5" cy="0.5" r="0.75">
          <stop offset="0" stop-color="var(--halftone)" stop-opacity="0.5"/>
          <stop offset="1" stop-color="var(--halftone)" stop-opacity="0.2"/>
        </radialGradient>
      </defs>
      <rect width="553" height="543" fill="var(--peach-light)"/>
      <rect width="553" height="543" fill="url(#rightTone)"/>
    </svg>
    <div class="page__text">
      <p>4. <span class="title">Hey, Hey Mama Rag</span> &nbsp; From Blind Blaine. The female vocals are spontaneous Nora, whose…well, girlishness…has kept the boys in the band from sounding…well, too darned <span class="title">male</span>…over the years. Sid’s great piano – and opening chuckle – set the tone.</p>
      <p>5. <span class="title">Kelsey Jaynes</span> &nbsp; Inspired by the Fuzzy Lowell classic spelled with a “K”.</p>
      <p>6. <span class="title">Creek Bank Blues</span> &nbsp; A real oldie, freshened up by Arlo’s jew’s harp and inimitable vocals.</p>
      <p>7. <span class="title">Pick It Up And Run</span> &nbsp; For years Mr. K’s go-to piece for a shot of adrenaline. Done live here…and – predictably – totally out of control, featuring Arlo’s <span class="title">are you kidding me?</span> harmonica chops. Stan Mercer plays the fastest mandolin solo this side of bluegrass.</p>
      <p>8. <span class="title">Sweet On My Darling</span> &nbsp; Learned by most of the band from Jim Kessler, but dating back to at least the 1920’s and Gus Canton. Mack’s great <span class="title">spike driver</span> and <span class="title">sugar</span> vocals.</p>
      <p>9. <span class="title">Down the Line Again</span> &nbsp; A wanton desecration of the Delta Crock Band.</p>
      <p>10. <span class="title">I Never Sighed</span> &nbsp; John Mallard’s great interpretation of Blind Toby Dorsey–also defiled.</p>
      <p>11. <span class="title">Harbor Town Blues</span> &nbsp; More Jesse Fulton. The unchallenged anthem of ‘60’s guitar pickers. Mack (also on jug) aids and abets Dale’s vocal depredations.</p>
      <p>12. <span class="title">Meet Me by the Levee</span> &nbsp; From a Jackie Warrington LP. Mack scolds Dale.</p>
      <p>13. <span class="title">You’re No Use</span> &nbsp; Jesse Fulton’s number – as usual, played too fast by a band that never did drugs, but always sounds like it’s on speed.</p>
      <p>14. <span class="title">Cousin Liza</span> &nbsp; Another Mr. K crowd-pleaser, osmosed from fellow musicians with guitars, fingerpicks, and bad attitudes. Unsurpassed kazoo solo by Boyd Walden.</p>
    </div>
  </section>
</div>
</body>
</html>
```